Luxurious Product label and box for all natural skincare product. + 30AUD tip to winner.

What I require.
1.     One product label and one-box design.
2.     I must have a mock-up of the bottle with the attached label and the box.
 
I have supplied the following files for the designers to use.
1.     Brand logo file. (logo.zip)
2.     Slogan file. (slogan.psd)
3.     Slogan script file. (italianno.regular.ttf)
4.     Bottle image file. (60ml_moisturiser_bottle.png)
5.     Icon bar file. (Icon_bar_en.zip)
 
Label and box Design
I am interested in your unique design concepts and colors, so please feel free to be creative.
1.     Brand name: Quenra
2.     You can use your own choice of colors in your design. I would prefer two colors (excluding logo and slogan colors), although more colors are acceptable for the right design.
3.     Label and box to have a background color or pattern.
4.     I would like the icon bar to wrap around the bottom of the label and box, covering the full width of all sides of the box.
5.     The height of the icon bar should be about 7mm to 10mm high.   
6.     The hex code for the icon bar color is #EDD6D4. The color of the icons can be any color the designer chooses.
7.     The positioning of the icons are as follows.
a)     The front panel has three icons. From left to right, they are; 100% Vegan, Product of Australia, and 100% Natural.
b)     The left side panel has three icons. From the front of the label/box to the back of the label/box, they are; Cruelty-Free, Ethical & Sustainable, and Please Recycle.
c)     The right side panel has only one icon situated at the front of the right side of the label/box. The icon is 6 Months Once Open.
 
Label.
1.     The label will be a three-panel label.
2.     The label will contain text in all three panels; however, only the text for the front panel of the label is supplied in this brief. For now, use Lorem Ipsum placeholder text to fill spaces.
3.     The final text will be provided to the winning designer so they can apply the text to the left and right panels of the label.
4.     Label size. Width 104mm x Height 83mm.
5.     The final design file must include bleed and cut lines.
 
Box.
1.     The box will contain text on all four sides; however, only the text for the front of the box is supplied in this brief. For now, use Lorem Ipsum placeholder text to fill spaces.
2.     The final text will be provided to the winning designer so they can apply the text to the left and right sides and the back of the box.
3.     The box size is 40mm wide x 40mm deep x 140mm high.
4.     The final design file must include bleed and cut lines.
 
Front Panel wording.
1.     Logo.
2.     Slogan.
3.     Moisturiser.
4.     Hydrate & Nourish.
5.     Hyaluronic Acid, Desert Lime & Green Tea.
6.     All Skin Types - Dry – Dehydrated.
7.     Icon bar.
8.     60mL
 
Bottle size
60ml White Bottle – 13.5cm High x 3.5cm Wide.

Target Market(s)

Beauty-minded Asian consumers between the age of 32 and 75 who take a proactive approach in maintaining younger-looking skin. Those who already know the danger of damaged skin caused by skincare containing harsh chemicals, and therefore choose effective natural/organic solutions to meet their skincare needs. Those who wish a more radiant glow and youthful appearance to their skin. Usually, a two-income middle to high-income bracket couple with a mindset for health and beauty.

Industry/Entity Type

Beauty and skincare.

Font styles to use
Other font styles liked:
• Logo and slogan script supplied. Designer to choose all other font or script.

Colors

Designer to choose colors to be used in the design.

Requirements
Must have
• A mock-up label on the bottle and a mock-up box. My logo and slogan are already designed with my chosen font and color.
Nice to have
• I like soft pastel colors with perhaps a small amount of stronger color.

```html
<!DOCTYPE html>
<html lang="en">
<head>
<meta charset="utf-8">
<title>Quenra Moisturiser Label</title>
<link rel="stylesheet" href="https://fonts.googleapis.com/css2?family=Arimo:wght@400;700&family=Italianno&display=swap">
<style>
  :root {
    --sky: #c6e6f3;
    --mist: #dfe9ee;
    --mint: #a8dbbf;
    --leaf: #3b8a4f;
    --slogan: #4c9f45;
    --wreath: #5f9a6a;
    --forest: #23472a;
    --ink: #3f4242;
    --ring: #8fb8e0;
    --brand: #c08a35;
    --white: #ffffff;
  }
  html, body {
    margin: 0;
    padding: 0;
    width: 1200px;
    height: 4205px;
    overflow: hidden;
  }
  .label {
    position: relative;
    width: 1200px;
    height: 4205px;
    background: linear-gradient(180deg, var(--sky) 0%, var(--mist) 45%, #cfe6df 70%, var(--mint) 100%);
    font-family: "Arimo", Arial, sans-serif;
    color: var(--ink);
  }
  .product-name {
    position: absolute;
    top: 420px;
    left: 0;
    width: 1200px;
    text-align: center;
    margin: 0;
    font-size: 138px;
    font-weight: 700;
    color: var(--leaf);
    letter-spacing: -1px;
  }
  .title-rule {
    position: absolute;
    top: 614px;
    left: 140px;
    width: 920px;
    height: 5px;
    background: var(--forest);
  }
  .benefit {
    position: absolute;
    top: 643px;
    left: 310px;
    margin: 0;
    font-size: 77px;
    color: var(--forest);
    white-space: nowrap;
  }
  .wreath {
    position: absolute;
    top: 1315px;
    left: 92px;
    width: 1016px;
    height: 1016px;
  }
  .brand-mark {
    position: absolute;
    top: 1309px;
    left: 89px;
    width: 1029px;
    height: 1029px;
  }
  .brand-name {
    position: absolute;
    top: 1750px;
    left: 0;
    width: 1200px;
    text-align: center;
    font-size: 130px;
    font-weight: 400;
    color: var(--brand);
    line-height: 1;
  }
  .slogan {
    position: absolute;
    top: 2345px;
    left: 0;
    width: 1200px;
    text-align: center;
    margin: 0;
    font-family: "Italianno", cursive;
    font-size: 200px;
    line-height: 1;
    color: var(--slogan);
  }
  .ingredients {
    position: absolute;
    top: 2610px;
    left: 0;
    width: 1200px;
    text-align: center;
    margin: 0;
    font-size: 68px;
    line-height: 84px;
    color: var(--ink);
  }
  .icon-bar {
    position: absolute;
    top: 3200px;
    left: 0;
    width: 1200px;
    height: 230px;
  }
  .icon {
    position: absolute;
    width: 200px;
    text-align: center;
    font-size: 30px;
    font-weight: 700;
    line-height: 38px;
    color: var(--ink);
  }
  .icon svg { display: block; margin: 0 auto 12px; }
  .icon-vegan { left: 286px; }
  .icon-origin { left: 500px; }
  .icon-natural { left: 696px; }
  .skin-band {
    position: absolute;
    top: 3515px;
    left: 0;
    width: 1200px;
    height: 196px;
    background: var(--forest);
    color: var(--white);
    font-size: 56px;
    display: flex;
    align-items: center;
    justify-content: center;
  }
  .volume {
    position: absolute;
    top: 3757px;
    left: 0;
    width: 1200px;
    text-align: center;
    font-size: 80px;
    color: #2e2e2e;
  }
</style>
</head>
<body>
<main class="label">
  <h1 class="product-name">MOISTURISER</h1>
  <div class="title-rule"></div>
  <p class="benefit">Hydrate &amp; Nourish</p>

  <svg class="wreath" viewBox="0 0 1016 1016" role="img" aria-label="Circular wreath of green leafy branches with small dots framing the brand name">
    <defs>
      <radialGradient id="wreathTone" cx="50%" cy="50%" r="50%">
        <stop offset="76%" stop-color="var(--wreath)" stop-opacity="0"/>
        <stop offset="88%" stop-color="var(--wreath)" stop-opacity="0.32"/>
        <stop offset="100%" stop-color="var(--wreath)" stop-opacity="0"/>
      </radialGradient>
    </defs>
    <circle cx="508" cy="508" r="508" fill="url(#wreathTone)"/>
  </svg>

  <svg class="brand-mark" viewBox="0 0 1029 1029" aria-hidden="true">
    <circle cx="514" cy="514" r="300" fill="none" stroke="var(--ring)" stroke-width="6"/>
  </svg>
  <div class="brand-name">Quenra</div>

  <p class="slogan">grown by nature</p>

  <p class="ingredients">HYALURONIC ACID,DESERT<br>LIME &amp; GREEN TEA.</p>

  <section class="icon-bar">
    <div class="icon icon-vegan">
      <svg width="110" height="120" viewBox="0 0 110 120" aria-hidden="true">
        <path d="M55 110 C20 75 8 55 8 35 C8 18 20 8 33 8 C44 8 51 15 55 25 C59 15 66 8 77 8 C90 8 102 18 102 35 C102 55 90 75 55 110 Z" fill="none" stroke="var(--ink)" stroke-width="7"/>
      </svg>
      100%<br>Vegan
    </div>
    <div class="icon icon-origin">
      <svg width="200" height="120" viewBox="0 0 200 120" role="img" aria-label="Product of Australia icon">
        <rect x="20" y="20" width="160" height="90" rx="20" fill="#9fb3ab" opacity="0.6"/>
      </svg>
      Product of<br>Australia
    </div>
    <div class="icon icon-natural">
      <svg width="160" height="120" viewBox="0 0 160 120" aria-hidden="true">
        <g fill="none" stroke="var(--ink)" stroke-width="7" stroke-linejoin="round">
          <path d="M80 110 C55 90 55 45 80 10 C105 45 105 90 80 110 Z"/>
          <path d="M72 110 C40 110 15 85 12 50 C45 55 70 80 72 110 Z"/>
          <path d="M88 110 C120 110 145 85 148 50 C115 55 90 80 88 110 Z"/>
        </g>
      </svg>
      100%<br>Natural
    </div>
  </section>

  <div class="skin-band">All Skin Types - Dry – Dehydrated</div>
  <div class="volume">60 ml</div>
</main>
</body>
</html>
```